Horse related business entrepreneur needs a business card

I need a business card design for my horse related business. The enterprise is Tall Fern LLC and I have 3 businesses (headquartered at 2 locations): 1. property management where we rent horse stalls and apartments at a thoroughbred training center outside Ocala; 2. a medium sized transportation service in central Florida that sells horse bedding and removes used horse bedding from horse farms; and horse racing

```html
<!DOCTYPE html>
<html lang="en">
<head>
<meta charset="UTF-8">
<title>Tall Fern LLC – Business Card</title>
<link href="https://fonts.googleapis.com/css2?family=Michroma&family=Arimo:wght@400;700&display=swap" rel="stylesheet">
<style>
  :root {
    --stage: #1d1d1d;
    --card-dark: #121212;
    --card-light: #ffffff;
    --ink: #222226;
    --brand-red: #c8412b;
    --brand-orange: #e2603a;
    --swoosh: #3a383d;
    --text-light: #f2f2f2;
  }
  * { margin: 0; padding: 0; box-sizing: border-box; }
  html, body {
    width: 1200px; height: 1200px; overflow: hidden;
    background: var(--stage);
  }
  .canvas { position: relative; width: 1200px; height: 1200px; }
  .card {
    position: absolute; left: 170px; width: 860px; height: 491px;
    border-radius: 22px; overflow: hidden;
  }
  .card--back { top: 90px; background: var(--card-dark); }
  .card--front { top: 611px; background: var(--card-light); }

  /* Back side */
  .back-emblem {
    position: absolute; left: 330px; top: 70px; width: 200px; height: 200px;
    border-radius: 50%;
    background: radial-gradient(circle at 35% 30%, var(--brand-orange), var(--brand-red));
  }
  .back-brand {
    position: absolute; left: 0; right: 0; top: 300px; text-align: center;
    font-family: "Michroma", sans-serif; font-size: 40px; color: var(--text-light);
  }
  .back-addresses {
    position: absolute; left: 0; right: 0; top: 375px; text-align: center;
    font-family: "Arimo", sans-serif; font-size: 19px; line-height: 1.45; color: var(--text-light);
  }

  /* Front side */
  .front-emblem {
    position: absolute; left: 50px; top: 40px; width: 280px; height: 280px;
    border-radius: 50%;
    background: radial-gradient(circle at 35% 30%, var(--brand-orange), var(--brand-red));
  }
  .front-identity {
    position: absolute; right: 60px; top: 70px; text-align: right;
    font-family: "Michroma", sans-serif;
  }
  .front-identity .brand { font-size: 40px; color: var(--ink); }
  .front-identity .person { font-size: 28px; color: var(--ink); margin-top: 6px; }
  .front-identity .role { font-size: 20px; color: var(--brand-red); margin-top: 2px; }
  .front-wave { position: absolute; left: 0; top: 0; width: 860px; height: 491px; }
  .contact-list {
    position: absolute; right: 55px; bottom: 24px; list-style: none;
    font-family: "Arimo", sans-serif; font-size: 22px; color: var(--text-light);
  }
  .contact-list li {
    display: flex; justify-content: flex-end; align-items: center; gap: 14px; line-height: 1.5;
  }
  .contact-list svg { width: 22px; height: 22px; fill: var(--text-light); }
</style>
</head>
<body>
<main class="canvas">

  <section class="card card--back">
    <div class="back-emblem"></div>
    <div class="back-brand">TALL FERN LLC</div>
    <div class="back-addresses">
      <p>1520 SE Meadow Lane, Oakfield, FL 32600</p>
      <p>872 Willow Run Road, Hartsburg, VA 22900</p>
    </div>
  </section>

  <section class="card card--front">
    <svg class="front-wave" viewBox="0 0 860 491" aria-hidden="true">
      <defs>
        <linearGradient id="bandGradient" x1="0" y1="0" x2="1" y2="0">
          <stop offset="0" stop-color="#c2432f"/>
          <stop offset="0.5" stop-color="#b84632"/>
          <stop offset="1" stop-color="#e2573a"/>
        </linearGradient>
      </defs>
      <path d="M0,320 C230,420 500,330 860,255 L860,288 C500,330 240,440 0,350 Z" fill="var(--swoosh)"/>
      <path d="M0,365 C240,450 520,340 860,300 L860,491 L0,491 Z" fill="url(#bandGradient)"/>
      <path d="M20,372 C260,445 520,350 840,310" fill="none" stroke="#ffffff" stroke-width="3"/>
    </svg>

    <div class="front-emblem"></div>

    <div class="front-identity">
      <div class="brand">TALL FERN LLC</div>
      <div class="person">DANA WHITCOMB</div>
      <div class="role">OWNER</div>
    </div>

    <ul class="contact-list">
      <li>(555) 014-2290
        <svg viewBox="0 0 24 24"><path d="M6.6 10.8a15.1 15.1 0 0 0 6.6 6.6l2.2-2.2a1 1 0 0 1 1-.25 11.4 11.4 0 0 0 3.6.57 1 1 0 0 1 1 1V20a1 1 0 0 1-1 1A17 17 0 0 1 3 4a1 1 0 0 1 1-1h3.5a1 1 0 0 1 1 1c0 1.250.2 2.45.57 3.6a1 1 0 0 1-.25 1z"/></svg>
      </li>
      <li>(555) 014-7713
        <svg viewBox="0 0 24 24"><path d="M6 2h12v5H6zM4 8h16a2 2 0 0 1 2 2v6h-4v5H6v-5H2v-6a2 2 0 0 1 2-2zm4 8v3h8v-3z"/></svg>
      </li>
      <li>dana@tallfern.com
        <svg viewBox="0 0 24 24"><path d="M2 5h20v14H2zm2 2v.4l8 5.2 8-5.2V7zm0 2.8V17h16V9.8l-8 5.2z"/></svg>
      </li>
    </ul>
  </section>

</main>
</body>
</html>
```